Flyer Design For Building & Decorating Company

We need an A6 double-sided colour flyer for a letter-box marketing campaign. We are a building and decorating company based in West London. We saw a flyer that we liked and have attached it as an example of the sort of thing we're looking for (see attached files Example A6 Flyer - Front.png and Example A6 Flyer - Back.png). Please note that we're not expecting the designer to slavishly follow this design, more to use it as a jumping-off point.

The design must incorporate a strong call to action, e.g., Call Us For A Free, No-Obligation Quote.

The textual information that must be included in the flyer (contact methods, tagline, services, etc.) are included in the attached file Flyer Text.docx.

Also included as attachments are a selection of images used on our website (files bathroom.png, carpentry.png, decorating.jpg,
flooring.jpg, painting_decorating.jpg, repointing.jpg and work_ on_scaffold.jpg). Please include these images on the flyer (at least one image on each side), or use stock images if any of these are unsuitable.

The company logo will also need to be included in the flyer - see attached file logo.png

The images on our website have all had to be re-sized from the originals. I've attached a number of the original images to this brief, as these are the highest resolution versions of the images that we have. I would ask that you use the versions attached to the brief, but if you feel that other images from our website would work better on your flyer design, please let me know and I'll attach them to this brief.

Finally, we've attached guideline notes from our printer (see attached file Printer's Requirements.docx) - please ensure these are adhered to where relevant.

Target Market(s)

People in West London who require building or decorating work to be done on their properties.

Industry/Entity Type

Marketing

Requirements
Must have
• A6 double-sided colour flyer using the text we provided and some of the images provided.

The call to action must be prominent and eye-catching, as the only purpose of the flyer is to get recipients to contact our company for a quote.

```html
<!DOCTYPE html>
<html lang="en">
<head>
<meta charset="utf-8">
<title>Oakline Renovations – A6 Flyer</title>
<link rel="stylesheet" href="https://fonts.googleapis.com/css2?family=Cabin:ital,wght@0,400;0,500;0,700;1,700&display=swap">
<style>
  :root{
    --red:#fc3404;
    --band:#f76c45;
    --pale:#eef8d2;
    --white:#ffffff;
    --gold:#d8b36a;
    --page:#ffffff;
  }
  *{box-sizing:border-box;margin:0;padding:0}
  html,body{width:1200px;height:1000px;overflow:hidden;background:var(--page)}
  body{font-family:"Cabin",Arial,sans-serif;color:var(--white);position:relative}

  .side{position:absolute;top:118px;height:766px;background:var(--red)}
  .front{left:32px;width:550px}
  .back{left:617px;width:551px}

  /* front */
  .brand{position:absolute;left:36px;top:40px;width:140px;height:110px;display:flex;flex-direction:column;align-items:center;justify-content:center;gap:8px}
  .brand-mark{width:18px;height:18px;background:var(--gold)}
  .brand-name{font-weight:700;font-size:22px;line-height:1.1;color:var(--gold);text-align:center}
  .tagline{position:absolute;left:180px;top:44px;width:350px;text-align:center;font-style:italic;font-weight:700;font-size:20px;line-height:26px;letter-spacing:1.2px;text-transform:uppercase}
  .contact-band{position:absolute;left:0;top:180px;width:100%;height:54px;background:var(--band);text-align:center;font-size:15px;line-height:21px;padding-top:6px;letter-spacing:.3px}
  .contact-band .web{margin-left:18px}
  .photo{position:absolute;border:3px solid var(--white)}
  .photo-kitchen{left:40px;top:254px;width:221px;height:148px;background:linear-gradient(135deg,#5a4a34,#c9b690 55%,#6b5a3d)}
  .photo-flooring{left:288px;top:254px;width:218px;height:148px;background:linear-gradient(120deg,#e8ddd0,#c99858 55%,#a46d36)}
  .services{position:absolute;left:0;top:426px;width:100%;text-align:center;font-weight:700;font-size:17px;line-height:26.5px;letter-spacing:.6px}
  .cta{position:absolute;left:0;top:525px;width:100%;height:241px;background:var(--pale);color:var(--red)}
  .cta-line{position:absolute;left:30px;top:20px;font-weight:700;font-size:29px;line-height:34px;text-transform:uppercase}
  .cta-tick{position:absolute;left:456px;top:16px}
  .phone-icon{position:absolute;left:28px;top:110px}
  .numbers{position:absolute;left:126px;top:98px;font-weight:700;font-size:55px;line-height:58px;letter-spacing:2px}

  /* back */
  .row{position:absolute;left:0;width:100%}
  .row-band{position:absolute;left:0;top:0;height:100%;background:var(--band);width:305px}
  .row-text{position:absolute;left:32px;top:10px;font-size:15px;line-height:20px}
  .row-title{font-weight:700;font-size:16px;letter-spacing:1px;text-transform:uppercase;line-height:20px;margin-bottom:1px}
  .row-img{position:absolute;left:308px;top:0;width:190px;height:100%}
  .r1{top:17px;height:133px}
  .r2{top:166px;height:132px}
  .r3{top:313px;height:132px}
  .r4{top:460px;height:134px}
  .r5{top:609px;height:135px}
  .r3 .row-text{font-size:16px;line-height:21.5px;top:10px}
  .r3 .row-title{font-size:17px}
  .r4 .row-text{font-size:14px;line-height:19.5px}
  .r5 .row-text{font-size:13px;line-height:17.5px;left:30px;top:8px}
  .r5 .row-band{width:196px}
  .r5 .row-img{left:196px;width:129px}
  .img-bath{background:linear-gradient(135deg,#dfe6ee,#3f5d8c 45%,#8a6a45)}
  .img-carpentry{background:linear-gradient(135deg,#c9ad88,#e6d3b1 50%,#caa030)}
  .img-roof{background:linear-gradient(160deg,#9aa28a,#4b4d4f 50%,#3a3b3d)}
  .img-house{background:linear-gradient(160deg,#b7b8b5,#8a3b2a 50%,#3d4a35)}
  .img-cornice{background:linear-gradient(135deg,#efeae2,#d2c3b0 60%,#b98f78)}
  .more{position:absolute;left:360px;top:624px;font-weight:700;font-size:37px;line-height:42px;letter-spacing:1px}
  .more .small{font-size:25px}
</style>
</head>
<body>

<section class="side front">
  <div class="brand">
    <span class="brand-mark"></span>
    <span class="brand-name">Oakline Renovations</span>
  </div>
  <p class="tagline">‘West London Builders &amp; Decorators<br>Quality Renovations at Affordable Prices’</p>
  <div class="contact-band">
    Oakline Renovations, 14 Larch Grove, Ealing, London W5 9QT<br>
    Email: hello@oakline-renovations.co.uk<span class="web">Web: www.oakline-renovations.co.uk</span>
  </div>
  <div class="photo photo-kitchen" role="img" aria-label="Photo of a renovated fitted kitchen with window"></div>
  <div class="photo photo-flooring" role="img" aria-label="Photo of hands measuring and marking vinyl flooring"></div>
  <p class="services">
    Bathroom/Kitchens &nbsp;•&nbsp; Tiling &nbsp;•&nbsp; Painting/Decorating<br>
    Plastering &nbsp;•&nbsp; Carpentry &nbsp;•&nbsp; Flooring &nbsp;•&nbsp; Plumbing<br>
    Electrical Works &nbsp;•&nbsp; Brickwork &nbsp;•&nbsp; General Repairs
  </p>
  <div class="cta">
    <p class="cta-line">Call us now for a free<br>no-obligation quote</p>
    <svg class="cta-tick" width="64" height="64" viewBox="0 0 64 64" aria-hidden="true">
      <circle cx="30" cy="34" r="26" fill="none" stroke="var(--red)" stroke-width="5"/>
      <path d="M16 34 L28 47 L56 6" fill="none" stroke="var(--red)" stroke-width="7" stroke-linecap="round" stroke-linejoin="round"/>
    </svg>
    <svg class="phone-icon" width="80" height="80" viewBox="0 0 80 80" aria-hidden="true">
      <circle cx="40" cy="40" r="36" fill="none" stroke="var(--red)" stroke-width="5"/>
      <path d="M28 20c3-2 6-1 7 2l3 8c1 2 0 4-2 5l-3 2c2 6 6 10 12 13l2-3c1-2 3-3 5-2l8 3c3 1 4 4 2 7l-3 4c-3 3-8 3-13 1-10-5-18-13-23-24-2-5-1-10 2-13z" fill="var(--red)"/>
    </svg>
    <p class="numbers">0208 946 0183<br>07700 900417</p>
  </div>
</section>

<section class="side back">
  <div class="row r1">
    <div class="row-band"></div>
    <div class="row-text">
      <p class="row-title">Bathroom/Kitchen</p>
      - Complete/Partial Fixings<br>- Tiling<br>- Sink/Bath/Radiator<br>- Tap Repairs/Replace<br>- Fit Washing Machine/Dishwasher
    </div>
    <div class="row-img img-bath" role="img" aria-label="Photo of a bathroom with blue panelling and bath"></div>
  </div>
  <div class="row r2">
    <div class="row-band"></div>
    <div class="row-text">
      <p class="row-title">Carpentry</p>
      - Wardrobes/Cupboards<br>- Shelving/Skirting<br>- Doors/Windows<br>- Kitchen/Bathroom Suites<br>- Wooden Floor/Laminate
    </div>
    <div class="row-img img-carpentry" role="img" aria-label="Photo of a carpenter marking timber beside a hammer"></div>
  </div>
  <div class="row r3">
    <div class="row-band"></div>
    <div class="row-text">
      <p class="row-title">Maintenance/Repairs</p>
      - Reseal Bath/Shower<br>- Fit Shelves<br>- Electrics - Complete/Partial<br>- Sash/Gutter/Roof Repairs
    </div>
    <div class="row-img img-roof" role="img" aria-label="Photo of workers laying felt on a flat roof"></div>
  </div>
  <div class="row r4">
    <div class="row-band"></div>
    <div class="row-text">
      <p class="row-title">Landscape/Roof/<br>Work on High Ladders:</p>
      - Fencing/Paving/Decking<br>- Work On High Ladders/Scaffold<br>- Tree Cutting/Removal<br>- Roofing - New/Repair
    </div>
    <div class="row-img img-house" role="img" aria-label="Photo of a red brick house front with ladder"></div>
  </div>
  <div class="row r5">
    <div class="row-band"></div>
    <div class="row-text">
      <p class="row-title">Decorating</p>
      - Complete/Partial Works<br>- Lining/Wallpaper<br>- Painting Inside/Outside<br>- Plastering/Skimming<br>- Rectify Damage<br>- Freshen Paintwork
    </div>
    <div class="row-img img-cornice" role="img" aria-label="Photo of hands fitting ceiling coving"></div>
    <p class="more"><span class="small">AND</span><br>LOTS<br>MORE...</p>
  </div>
</section>

</body>
</html>
```